Medical IT Business with New logo needs a fresh stationary design

First time on pixel Harbor; Thought I would give it a go.
This project is for business cards alone but we have loads of design work that needs to take place in the immediate future.

We provide IT services to the Medical Industry and value ourselves as offering a premium product to the market.

I am after a fresh, clean design using full colour 2 sided cards which includes our current colour palettes from our logo.

Card's must include:
- Logo
- Slogan
- Name
- Adress
- Email
- Phone
- Fax
- Mobile

Target Market(s)

Surgeons, High Profile Medical Personnel

Industry/Entity Type

Business

Fonts, CMYK Colours and Logo files attached.

Requirements
Must have
• Card's must include:
• - Logo
• - Slogan
• - Name
• - Adress
• - Email
• - Phone
• - Fax
• - Mobile
Nice to have
• Needs to incorporate our colour palette (attached CMYK colours)
Should not have
• Black backgrounds. Black text ok.

```html
<!DOCTYPE html>
<html lang="en">
<head>
<meta charset="utf-8">
<title>Clinivault Systems – Business Card</title>
<link rel="stylesheet" href="https://fonts.googleapis.com/css2?family=Open+Sans:wght@400;700&family=Arimo:wght@400;700&display=swap">
<style>
  :root {
    --bg: #e9ebee;
    --card: #ffffff;
    --navy: #123f7c;
    --sky: #1b7fbf;
    --grey-text: #7a8590;
    --white: #ffffff;
  }
  * { box-sizing: border-box; margin: 0; padding: 0; }
  html, body { width: 1200px; height: 997px; overflow: hidden; }
  body {
    background: var(--bg);
    font-family: "Arimo", Arial, sans-serif;
    position: relative;
  }
  .card {
    position: absolute;
    width: 520px;
    height: 300px;
    background: var(--card);
    border-radius: 18px;
    overflow: hidden;
    box-shadow: 0 10px 30px rgba(0,0,0,.18);
    top: 348px;
  }
  .card--front { left: 50px; }
  .card--back { left: 630px; }
  .card__bands { position: absolute; inset: 0; width: 100%; height: 100%; }

  .brand { position: absolute; display: flex; align-items: center; gap: 12px; }
  .brand__dot { border-radius: 50%; background: var(--sky); flex: none; }
  .brand__name {
    font-family: "Open Sans", Arial, sans-serif;
    font-weight: 700;
    color: var(--navy);
    line-height: 1.05;
    letter-spacing: .5px;
    white-space: nowrap;
  }
  .brand__slogan {
    font-family: "Open Sans", Arial, sans-serif;
    color: var(--grey-text);
    margin-top: 2px;
    white-space: nowrap;
  }

  .card--front .brand {
    left: 90px; top: 40px; width: 240px;
    flex-direction: column; gap: 10px; text-align: center;
  }
  .card--front .brand__dot { width: 86px; height: 86px; }
  .card--front .brand__name { font-size: 27px; }
  .card--front .brand__slogan { font-size: 14px; }

  .website {
    position: absolute;
    right: 10px; top: 170px;
    color: var(--white);
    font-size: 12px; font-weight: 700;
    letter-spacing: .6px;
    white-space: nowrap;
    transform: rotate(-34deg);
    transform-origin: right center;
  }

  .card--back .brand { right: 26px; top: 30px; }
  .card--back .brand__dot { width: 46px; height: 46px; }
  .card--back .brand__name { font-size: 17px; }
  .card--back .brand__slogan { font-size: 9.5px; }

  .person { position: absolute; left: 26px; top: 96px; }
  .person__name { color: var(--navy); font-weight: 700; font-size: 19px; }
  .person__role { color: var(--sky); font-size: 13px; margin-top: 2px; }

  .contacts {
    position: absolute; left: 22px; bottom: 12px;
    list-style: none;
    color: var(--white);
    font-size: 13.5px;
  }
  .contacts li { display: flex; align-items: center; gap: 9px; height: 17.5px; }
  .contacts svg { width: 14px; height: 14px; flex: none; }
</style>
</head>
<body>

<section class="card card--front" aria-label="Card front">
  <svg class="card__bands" viewBox="0 0 520 300" preserveAspectRatio="none" aria-hidden="true">
    <path d="M220,300 Q400,220 520,90 L520,300 Z" fill="var(--navy)"/>
    <path d="M205,300 Q390,212 508,80 L520,70 L520,84 Q400,214 230,300 Z" fill="var(--sky)"/>
  </svg>
  <div class="brand">
    <span class="brand__dot"></span>
    <div>
      <div class="brand__name">CLINIVAULT<br>SYSTEMS</div>
      <div class="brand__slogan">care that stays connected</div>
    </div>
  </div>
  <div class="website">www.clinivaultsystems.com</div>
</section>

<section class="card card--back" aria-label="Card back">
  <svg class="card__bands" viewBox="0 0 520 300" preserveAspectRatio="none" aria-hidden="true">
    <path d="M0,206 Q260,148 520,168 L520,300 L0,300 Z" fill="var(--navy)"/>
    <path d="M0,196 Q250,128 470,152 Q260,140 0,203 Z" fill="var(--sky)"/>
  </svg>
  <div class="brand">
    <span class="brand__dot"></span>
    <div>
      <div class="brand__name">CLINIVAULT SYSTEMS</div>
      <div class="brand__slogan">care that stays connected</div>
    </div>
  </div>
  <div class="person">
    <div class="person__name">Mara Keating</div>
    <div class="person__role">Director</div>
  </div>
  <ul class="contacts">
    <li><svg viewBox="0 0 14 14"><circle cx="7" cy="7" r="7" fill="#c9d4e2"/><path d="M4 4.5 L5.6 4 L6.4 5.8 L5.6 6.5 Q6.4 8 7.6 8.6 L8.3 7.8 L10 8.6 L9.5 10.2 Q6.5 10.2 4 6.8 Z" fill="var(--navy)"/></svg>0412 308 551</li>
    <li><svg viewBox="0 0 14 14"><circle cx="7" cy="7" r="7" fill="#c9d4e2"/><rect x="3.5" y="6" width="7" height="4.5" rx=".6" fill="var(--navy)"/><rect x="5" y="3.5" width="4" height="2.5" fill="var(--navy)"/></svg>0298 774 160</li>
    <li><svg viewBox="0 0 14 14"><circle cx="7" cy="7" r="7" fill="#c9d4e2"/><rect x="5" y="3" width="4" height="8" rx=".8" fill="var(--navy)"/></svg>0433 915 207</li>
    <li><svg viewBox="0 0 14 14"><circle cx="7" cy="7" r="7" fill="#c9d4e2"/><rect x="3.5" y="4.5" width="7" height="5" fill="var(--navy)"/><path d="M3.5 4.5 L7 7.3 L10.5 4.5" stroke="#c9d4e2" stroke-width=".8" fill="none"/></svg>care@clinivault.com.au</li>
    <li><svg viewBox="0 0 14 14"><circle cx="7" cy="7" r="7" fill="#c9d4e2"/><path d="M7 11 Q4 7.5 4 6 A3 3 0 0 1 10 6 Q10 7.5 7 11 Z" fill="var(--navy)"/><circle cx="7" cy="6" r="1" fill="#c9d4e2"/></svg>Unit 4, 27 Harlow Road, Elmvale</li>
  </ul>
</section>

</body>
</html>
```